political campaign tax exemption on school taxes that dont have kids in the district

Harlow Vale School Board Races

Taxes, Taxes, Taxes!
Everyone pays them!
You have tax exemption for the elderly.
You have tax exemption for the veterans.
What about tax exemptions for you?

In Texas, a governing entity, has the option of giving a 20 percent tax exemption. Our current school board, hasnt offered it you! We will!

Can we count on your vote? You can count on ours!
small discloure (political ad paid by candidates)

attached are the candidates for this exemption

Political

• need to include disclaimer at bottom.

political ad paid by candidate

```html
<!DOCTYPE html>
<html lang="en">
<head>
<meta charset="utf-8">
<title>Harlow Vale School Board – Tax Exemption</title>
<link rel="stylesheet" href="https://fonts.googleapis.com/css2?family=Archivo+Black&family=Arimo:ital,wght@1,400;1,700&family=Open+Sans:wght@400;600&family=Oswald:wght@600&family=PT+Sans&family=Roboto+Condensed:wght@700&display=swap">
<style>
  :root {
    --navy: #2e3192;
    --ocean: #0d6db6;
    --sky: #3a9ad9;
    --red: #ed1c24;
    --orange: #f7941d;
    --grey: #a7a9ac;
    --ink: #111111;
    --white: #ffffff;
  }
  html, body {
    margin: 0;
    padding: 0;
    width: 1200px;
    height: 914px;
    overflow: hidden;
    background: var(--white);
  }
  .poster { display: block; width: 1200px; height: 914px; }
  .band-navy { fill: var(--navy); }
  .band-ocean { fill: var(--ocean); }
  .band-red { fill: var(--red); }
  .band-orange { fill: var(--orange); }
  .band-sky { fill: var(--sky); }
  .rule-red { fill: var(--red); }
  .rule-orange { fill: var(--orange); }
  .rule-white { fill: var(--white); }

  .headline { font-family: "Open Sans", sans-serif; font-weight: 600; fill: var(--white); }
  .article { font-family: "Open Sans", sans-serif; font-weight: 400; fill: var(--white); }
  .board-name { font-family: "Open Sans", sans-serif; font-weight: 400; fill: var(--grey); }
  .agency { font-family: "Open Sans", sans-serif; font-weight: 600; fill: var(--ink); }
  .lead-italic { font-family: "Arimo", sans-serif; font-style: italic; font-weight: 400; fill: var(--ink); }
  .option { font-family: "Arimo", sans-serif; font-weight: 700; fill: var(--white); }
  .exemption { font-family: "Arimo", sans-serif; font-style: italic; font-weight: 700; fill: var(--white); }
  .current { font-family: "Archivo Black", sans-serif; fill: var(--ink); }
  .hasnt { font-family: "Oswald", sans-serif; font-weight: 600; fill: var(--white); }
  .hasnt .you { fill: var(--orange); stroke: var(--white); stroke-width: 1.5px; paint-order: stroke; }
  .we-will { font-family: "Open Sans", sans-serif; font-weight: 400; fill: var(--red); }
  .list-title { font-family: "Roboto Condensed", sans-serif; font-weight: 700; fill: var(--white); }
  .list-item { font-family: "PT Sans", sans-serif; fill: var(--white); }
  .vote-ask { font-family: "Arimo", sans-serif; font-style: italic; font-weight: 400; fill: var(--white); }
  .vote-promise { font-family: "Roboto Condensed", sans-serif; font-weight: 700; fill: var(--white); }
  .disclaimer { font-family: "Arimo", sans-serif; font-weight: 400; fill: var(--ink); }
</style>
</head>
<body>
<svg class="poster" viewBox="0 0 1200 914" xmlns="http://www.w3.org/2000/svg" aria-label="Harlow Vale School Board campaign flyer">
  <!-- Headline row -->
  <rect class="band-navy" x="0" y="0" width="458" height="150"/>
  <text class="headline" x="16" y="118" font-size="96" textLength="422" lengthAdjust="spacingAndGlyphs">In Texas,</text>
  <rect class="band-sky" x="432" y="0" width="59" height="64"/>
  <text class="article" x="441" y="54" font-size="62">a</text>
  <text class="board-name" x="500" y="33" font-size="31" textLength="682" lengthAdjust="spacing">HARLOW VALE SCHOOL BOARD</text>
  <rect class="band-red" x="458" y="43" width="742" height="107"/>
  <text class="agency" x="478" y="124" font-size="80" textLength="702" lengthAdjust="spacingAndGlyphs">governing agnecy</text>

  <!-- Option row -->
  <rect class="band-ocean" x="0" y="150" width="1200" height="73"/>
  <rect class="band-navy" x="137" y="153" width="183" height="70"/>
  <text class="lead-italic" x="8" y="201" font-size="31" textLength="122" lengthAdjust="spacingAndGlyphs">has the</text>
  <text class="option" x="145" y="204" font-size="46" textLength="166" lengthAdjust="spacingAndGlyphs">option</text>
  <text class="lead-italic" x="325" y="201" font-size="31" textLength="176" lengthAdjust="spacingAndGlyphs">of giving a</text>
  <text class="exemption" x="512" y="205" font-size="50" textLength="664" lengthAdjust="spacingAndGlyphs">20 percent tax exemption</text>
  <text class="lead-italic" x="1180" y="205" font-size="40">.</text>

  <!-- Current board row -->
  <rect class="band-orange" x="0" y="223" width="423" height="132"/>
  <rect class="band-navy" x="423" y="223" width="777" height="132"/>
  <text class="current" x="28" y="287" font-size="52" textLength="370" lengthAdjust="spacingAndGlyphs">Our current</text>
  <text class="current" x="28" y="338" font-size="36" textLength="370" lengthAdjust="spacingAndGlyphs">SCHOOL BOARD</text>
  <text class="hasnt" x="434" y="318" font-size="64" textLength="748" lengthAdjust="spacingAndGlyphs">HASN’T OFFERED IT TO <tspan class="you">YOU!</tspan></text>
  <rect class="rule-white" x="636" y="324" width="230" height="3"/>
  <rect class="rule-orange" x="572" y="335" width="294" height="4"/>

  <!-- We will -->
  <rect class="rule-red" x="0" y="356" width="1200" height="5"/>
  <text class="we-will" x="12" y="593" font-size="306" textLength="1164" lengthAdjust="spacingAndGlyphs">WE WILL!</text>
  <rect class="rule-red" x="0" y="603" width="1200" height="6"/>

  <!-- Footer panels -->
  <rect class="band-navy" x="0" y="611" width="602" height="303"/>
  <rect class="band-ocean" x="602" y="611" width="598" height="303"/>

  <text class="list-title" x="22" y="686" font-size="28" textLength="254" lengthAdjust="spacingAndGlyphs">Taxes, Taxes, Taxes!</text>
  <text class="list-item" x="22" y="725" font-size="28">Everyone pays them!</text>
  <text class="list-item" x="22" y="768" font-size="28">You have tax exemption for the elderly.</text>
  <text class="list-item" x="22" y="810" font-size="28">You have tax exemption for the veterans.</text>
  <text class="list-title" x="22" y="856" font-size="28" textLength="488" lengthAdjust="spacingAndGlyphs">What about tax exemptions for you?</text>

  <text class="vote-ask" x="903" y="692" font-size="35" text-anchor="middle">Can we count on your vote?</text>
  <text class="vote-promise" x="905" y="750" font-size="38" text-anchor="middle">You can count on ours!</text>
  <text class="disclaimer" x="890" y="894" font-size="15" text-anchor="middle">Political ad paid by candidate.</text>
</svg>
</body>
</html>
```